Business card design needed

Family General Practitioner/ Family Physician.
Logo is the logo of the Crestmoor Guild of Family Clinicians Australia
http://kvplm.tarevo.edu.au/PictureGallery/logos/pages/CGFC%20logo_jpg.htm

Reason: Just a bit more time to make changes and the weekend for me to look at things closely and to choose. Thanks, Lumi

Thanks for all the submissions. So many of them are really works of art. Not one of them are not good. The ones that I am eliminating are the ones that I think are not suitable for me personally only, and because if I don't, it makes it very difficult to decide as many of you are also sending me slight variations of a card. I have just decided to choose a second place card too. Can't thank you all enough. Good luck, Lumi. P.S - Working today till 10 pm as the card says :-), so probably won't be able to give a feedback till late Saturday night or Sunday morning here in Sydney, Australia. 

Reason: Just added a second place to the budget and realised that Australia is ahead of the rest of the world in the time zone (only :-) - don't want to offend anyone or start a debate!! ) , so Monday deadline will mean it will be a weekend for the rest of the world. Just wanted to give everyone more time to submit their best, especially since I will be picking a second card too. Can't thank everyone enough for the submissions. P.S - Not keen on photos on the card.

Contact Information for Business Card

Dr. Lumi Harcourt M.B.B.S., F.C.G.F.C
Family General Practitioner
Address, timings, phone and fax number on the back.

Requirements
Must have
• Timings
Mon 7 am - 7 pm
Tues 7 am - 12 pm
Wed 7 am - 10 pm
Thurs 7 am - 12 pm
Fri 7 am - 8 pm
Sat 8 am - 10 pm
Sun - Off

```html
<!DOCTYPE html>
<html lang="en">
<head>
<meta charset="utf-8">
<title>Dr. Lumi Harcourt – Business Card</title>
<link rel="stylesheet" href="https://fonts.googleapis.com/css2?family=Montserrat:wght@300;400;500&display=swap">
<style>
  :root {
    --backdrop: #e9ecef;
    --card-white: #f7fbfe;
    --card-sky: #a9d3f0;
    --card-blue: #6bb6e6;
    --strip-blue: #bfe0f6;
    --band-blue: #57a9df;
    --band-deep: #3d96d4;
    --ink-blue: #2f7fc4;
    --ink-soft: #4b9ad6;
    --ink-dark: #1d2a36;
    --rule: #7d9fb8;
    --icon: #d98a2b;
  }
  * { box-sizing: border-box; margin: 0; padding: 0; }
  html, body {
    width: 1200px; height: 1051px; overflow: hidden;
    background: var(--backdrop);
    font-family: "Montserrat", sans-serif;
  }
  .sheet {
    width: 1200px; height: 1051px;
    display: flex; flex-direction: column; align-items: center; justify-content: center;
    gap: 30px;
  }
  .card {
    position: relative;
    width: 780px; height: 472px;
    overflow: hidden;
    box-shadow: 0 6px 18px rgba(0,0,0,.15);
  }
  .card::after {
    content: ""; position: absolute; inset: 0; pointer-events: none;
    background: repeating-linear-gradient(135deg, rgba(255,255,255,.10) 0 2px, rgba(255,255,255,0) 2px 6px);
  }

  /* Front */
  .card-front {
    background: linear-gradient(160deg, var(--card-white) 0%, #d8ecfa 35%, var(--card-sky) 70%, var(--card-blue) 100%);
  }
  .front-name {
    position: absolute; left: 150px; top: 120px;
    font-weight: 300; font-size: 58px; letter-spacing: 1px;
    color: #fff;
    text-shadow: 0 1px 2px rgba(40,90,140,.55);
  }
  .front-credentials {
    position: absolute; right: 110px; top: 196px;
    font-weight: 300; font-size: 21px; letter-spacing: 1px;
    color: #fff;
    text-shadow: 0 1px 2px rgba(40,90,140,.5);
  }
  .front-role {
    position: absolute; left: 150px; top: 262px;
    font-weight: 400; font-size: 25px;
    color: var(--ink-blue);
  }

  /* Back */
  .card-back {
    background: linear-gradient(165deg, #ffffff 0%, #e4f1fb 45%, #cfe7f7 100%);
  }
  .contact-strip {
    position: absolute; left: 0; top: 244px; width: 400px; height: 106px;
    background: linear-gradient(90deg, var(--strip-blue), rgba(191,224,246,0));
    border-top: 1px solid rgba(125,159,184,.6);
  }
  .back-band {
    position: absolute; left: 0; right: 0; bottom: 0; height: 122px;
    background: linear-gradient(180deg, var(--band-blue), var(--band-deep));
    border-top: 2px solid var(--rule);
  }
  .org-mark {
    position: absolute; left: 50px; top: 50px;
    width: 260px; height: 180px;
    display: flex; align-items: center; justify-content: center; gap: 14px;
  }
  .org-mark-square {
    width: 34px; height: 34px; background: var(--ink-blue);
  }
  .org-mark-name {
    font-weight: 400; font-size: 40px; letter-spacing: 3px; color: var(--ink-blue);
  }
  .hours-title {
    position: absolute; left: 420px; top: 36px;
    font-weight: 400; font-size: 30px; color: var(--ink-blue);
  }
  .hours-table {
    position: absolute; left: 420px; top: 86px;
    border-collapse: collapse;
    font-weight: 400; font-size: 20px;
  }
  .hours-table td { padding: 1px 0; line-height: 28px; }
  .hours-day { color: var(--ink-soft); width: 140px; }
  .hours-colon { color: var(--ink-dark); width: 26px; text-align: center; }
  .hours-time { color: var(--ink-dark); text-align: right; width: 150px; }

  .contact {
    position: absolute; left: 28px; top: 256px; width: 370px;
    font-style: normal; font-weight: 400; font-size: 14px; color: var(--ink-dark);
  }
  .contact-row { display: flex; align-items: flex-start; gap: 10px; margin-bottom: 8px; }
  .contact-row svg { flex: none; margin-top: 1px; }
  .contact-lines { line-height: 19px; }
  .contact-phone span + span { margin-left: 26px; }
</style>
</head>
<body>
<main class="sheet">

  <section class="card card-front" aria-label="Business card front">
    <h1 class="front-name">Dr. Lumi Harcourt</h1>
    <p class="front-credentials">M.B.B.S., F.C.G.F.C</p>
    <p class="front-role">Family General Practitioner</p>
  </section>

  <section class="card card-back" aria-label="Business card back">
    <div class="contact-strip"></div>
    <div class="back-band"></div>

    <div class="org-mark" role="img" aria-label="Crestmoor Guild of Family Clinicians Australia logo">
      <span class="org-mark-square"></span>
      <span class="org-mark-name">CGFC</span>
    </div>

    <h2 class="hours-title">Working Hours</h2>
    <table class="hours-table">
      <tr><td class="hours-day">Monday</td><td class="hours-colon">:</td><td class="hours-time">7am - 7pm</td></tr>
      <tr><td class="hours-day">Tuesday</td><td class="hours-colon">:</td><td class="hours-time">7am - 12pm</td></tr>
      <tr><td class="hours-day">Wednesday</td><td class="hours-colon">:</td><td class="hours-time">7am - 10pm</td></tr>
      <tr><td class="hours-day">Thursday</td><td class="hours-colon">:</td><td class="hours-time">7am - 12pm</td></tr>
      <tr><td class="hours-day">Friday</td><td class="hours-colon">:</td><td class="hours-time">7am - 8pm</td></tr>
      <tr><td class="hours-day">Saturday</td><td class="hours-colon">:</td><td class="hours-time">8am - 10pm</td></tr>
      <tr><td class="hours-day">Sunday</td><td class="hours-colon">:</td><td class="hours-time">Off</td></tr>
    </table>

    <address class="contact">
      <div class="contact-row">
        <svg width="18" height="18" viewBox="0 0 18 18" aria-hidden="true">
          <path d="M2 8 L9 2 L16 8 V16 H11 V11 H7 V16 H2 Z" fill="none" stroke="var(--icon)" stroke-width="1.8" stroke-linejoin="round"/>
        </svg>
        <div class="contact-lines">
          Lower Level, Harbour Arcade,<br>
          Wattle Grove Shopping Centre<br>
          Brindle Hill, NSW 2199
        </div>
      </div>
      <div class="contact-row contact-phone">
        <svg width="18" height="18" viewBox="0 0 18 18" aria-hidden="true">
          <path d="M4 2 L7 2 L8 6 L6 7.5 C7 10 8 11 10.5 12 L12 10 L16 11 L16 14 C16 15 15 16 14 16 C8 16 2 10 2 4 C2 3 3 2 4 2 Z" fill="var(--icon)"/>
        </svg>
        <div class="contact-lines"><span>P: 02 8411 5720</span><span>F: 02 8411 5738</span></div>
      </div>
    </address>
  </section>

</main>
</body>
</html>
```